Banner Ads Design Project

We need 3 new banner ads designed for the front page of our website. If you navigate to www.brightvane.net.au you will see there is a banner ad slider just underneath the menu at the top and we require 3 new designs created.
You will see that there is some text overlay at the right of the image, which is editable via our content management system. The background image therefore needs to be white in that area or at least very light as text will sit on top.
The image dimension is 940 x 335 and has beveled edges.
The 3 designs we require are as follows (note we don't just want to use pictures, we want more specific and custom designs created):
Desgin 1 - Radio Ad Link
BrightVane is currently running a radio campaign with Wave 94.7. We would like to advertise this on our website. See http://www.wave947.fm/win/cover-the-costs for an example of what we are after.
Design 2 - Special on LED's
We are running a special on LED lights at the moment. We need a design that includes an image of our LED light, which is attached. But also with some nice design elements, not just a picture of the light. I have attached a flyer we use for inspiration.
Design 3 - We want to advertise our new office in mitchell. So am simply after an image created using the attached photo of our office. That obviously has some white space at the right hand side so that I can overlay text.
Thanks,
Tobi

```html
<!DOCTYPE html>
<html lang="en">
<head>
<meta charset="utf-8">
<title>LED Lighting Banner</title>
<link rel="stylesheet" href="https://fonts.googleapis.com/css2?family=Roboto+Condensed:wght@400;700&family=Arimo:wght@400;700&display=swap">
<style>
  :root {
    --green-deep: #3aa000;
    --green-mid: #7cc82c;
    --green-text: #3f9a1c;
    --green-strong: #2f8a10;
    --navy: #173b6c;
    --body-text: #3a3a3a;
    --button-top: #3e5fa3;
    --button-bottom: #1f3b78;
    --white: #ffffff;
    --panel-line: #e4ecd8;
  }
  html, body {
    margin: 0;
    padding: 0;
    width: 1200px;
    height: 428px;
    overflow: hidden;
    background: var(--white);
  }
  .banner {
    position: relative;
    width: 1200px;
    height: 428px;
    border-radius: 8px;
    overflow: hidden;
    background:
      radial-gradient(ellipse 700px 420px at 120px 0px, var(--green-deep) 0%, var(--green-mid) 40%, rgba(200,232,160,0.6) 70%, rgba(255,255,255,0) 100%),
      linear-gradient(180deg, #e9f6dc 0%, var(--white) 90%);
  }
  .banner__visual-side {
    position: absolute;
    inset: 0 400px 0 0;
  }
  .banner__panel {
    position: absolute;
    top: 0;
    right: 0;
    width: 400px;
    height: 428px;
    background: linear-gradient(180deg, rgba(255,255,255,0.75) 0%, var(--white) 45%);
    border-left: 1px solid var(--panel-line);
  }
  .benefits {
    position: absolute;
    left: 48px;
    top: 104px;
    margin: 0;
    padding: 0;
    list-style: none;
    font-family: "Roboto Condensed", "Arial Narrow", sans-serif;
    font-size: 25px;
    color: var(--green-text);
  }
  .benefits li {
    position: relative;
    height: 38px;
    line-height: 38px;
    padding-left: 27px;
  }
  .benefits li::before {
    content: "";
    position: absolute;
    left: 0;
    top: 13px;
    width: 12px;
    height: 12px;
    border-radius: 50%;
    background: var(--green-strong);
  }
  .benefits strong { color: var(--green-strong); font-weight: 700; }
  .product-photo {
    position: absolute;
    left: 405px;
    top: 48px;
    width: 360px;
    height: 300px;
    border-radius: 50% 46% 44% 50%;
    background: radial-gradient(ellipse at 60% 45%, #f4f5f5 0%, #d7dadb 45%, #7c8084 75%, rgba(60,60,60,0.0) 100%);
  }
  .slider-arrow {
    position: absolute;
    left: 776px;
    top: 166px;
    width: 44px;
    height: 44px;
  }
  .panel-title {
    position: absolute;
    left: 69px;
    top: 66px;
    width: 300px;
    margin: 0;
    font-family: "Arimo", Arial, sans-serif;
    font-weight: 700;
    font-size: 20px;
    line-height: 25px;
    color: var(--navy);
  }
  .panel-text {
    position: absolute;
    left: 69px;
    top: 138px;
    width: 307px;
    margin: 0;
    font-family: "Arimo", Arial, sans-serif;
    font-size: 13.2px;
    line-height: 17px;
    text-align: justify;
    color: var(--body-text);
  }
  .store-button {
    position: absolute;
    left: 71px;
    top: 297px;
    width: 167px;
    height: 35px;
    border-radius: 3px;
    background: linear-gradient(180deg, var(--button-top) 0%, var(--button-bottom) 100%);
    color: var(--white);
    font-family: "Arimo", Arial, sans-serif;
    font-size: 13.5px;
    line-height: 35px;
    text-align: center;
    text-decoration: none;
  }
</style>
</head>
<body>
  <div class="banner">
    <div class="banner__visual-side">
      <ul class="benefits">
        <li><strong>Save up to 88%</strong> off lighting costs</li>
        <li><strong>Greater</strong> cost effectiveness</li>
        <li><strong>Very little</strong> heat emitted</li>
        <li><strong>More light</strong> emitted per watt</li>
        <li><strong>Highly</strong> durable</li>
        <li><strong>Environmentally</strong> friendly</li>
      </ul>
      <div class="product-photo" role="img" aria-label="Photo of a white LED downlight with a black heat-sink body"></div>
    </div>

    <aside class="banner__panel">
      <h2 class="panel-title">Lorem ipsum Dolor sit Adipiscing elit</h2>
      <p class="panel-text">Praesent posuere egestas velit, id tincidunt libero tristique eu. Aliquam posuere consectetur lorem. Aliquam eget fringilla urna. Sed facilisis nibh eu diam suscipit dictum. Vivamus id felis ac mauris iaculis elementum ut vel diam</p>
      <a class="store-button" href="#">Visit Online Store</a>
    </aside>

    <svg class="slider-arrow" viewBox="0 0 44 44" aria-label="Previous slide">
      <defs>
        <linearGradient id="arrowFill" x1="0" y1="0" x2="0" y2="1">
          <stop offset="0" stop-color="#f4f4f4"/>
          <stop offset="1" stop-color="#d4d4d4"/>
        </linearGradient>
      </defs>
      <circle cx="22" cy="22" r="21" fill="url(#arrowFill)" stroke="#cfcfcf"/>
      <path d="M25 15 L18 22 L25 29" fill="none" stroke="#2f5a96" stroke-width="4" stroke-linecap="round" stroke-linejoin="round"/>
    </svg>
  </div>
</body>
</html>
```